User help guide for software for investment bank

We need a professional design for our user help guides for new software we have written for our client. We develop visualization software for investment banks in Singapore mainly focused in the financial and risk management area. Our help guides are design to show them how the software works as well as promote our brand
Updates

Target Market(s)

Investment banking, risk management, finance

Industry/Entity Type

Bank

Requirements
Must have
• Content of document and logos
• Colour sheme
• Professional brouchure design
• Verindo and plunox logos on it
• Look at www.verindo-example.com for company looks and feel
• PLEASE USE COLOUR SCHEMES BELOW IN ATTACHMENT AND FOLLOW SIMILAR STYLE TO CLIENT ANNUAL REPORT

```html
<!DOCTYPE html>
<html lang="en">
<head>
<meta charset="utf-8">
<title>Web Editor Tool – User Roles and Restrictions</title>
<link href="https://fonts.googleapis.com/css2?family=Arimo:wght@400;700&display=swap" rel="stylesheet">
<style>
  :root {
    --brand-red: #e3212b;
    --ink: #1a1a1a;
    --paper: #ffffff;
    --table-head: #000000;
    --rule: #9a9a9a;
  }
  * { box-sizing: border-box; margin: 0; padding: 0; }
  html, body { width: 848px; height: 1200px; overflow: hidden; background: var(--paper); }
  body { font-family: "Arimo", Arial, sans-serif; color: var(--ink); }
  .page { position: relative; width: 848px; height: 1200px; }

  .section-band {
    position: absolute; left: 0; height: 35px;
    background: var(--brand-red); color: #fff;
    font-size: 20px; font-weight: 400;
    display: flex; align-items: center; padding-left: 58px;
  }
  .band-roles { top: 212px; width: 372px; }
  .band-restrictions { top: 824px; width: 442px; }

  .body-text { position: absolute; left: 60px; width: 725px; font-size: 12.6px; line-height: 17px; }
  .intro-roles { top: 265px; }
  .intro-restrictions { top: 881px; }

  .red-heading { position: absolute; left: 60px; color: var(--brand-red); font-size: 19.5px; font-weight: 400; }
  .heading-roles { top: 292px; }
  .heading-can-do { top: 953px; }

  .list { position: absolute; list-style: none; font-size: 12.6px; }
  .list li { position: relative; }
  .list li::before {
    content: ""; position: absolute; width: 5px; height: 5px; border-radius: 50%;
    background: var(--ink); top: 6px;
  }
  .role-list { left: 0; top: 0; }
  .role { position: absolute; left: 109px; font-weight: 700; }
  .role::before { left: -19px; }
  .perm { position: absolute; left: 160px; font-weight: 400; }
  .perm::before { left: -18px; }

  .can-do-list { left: 160px; top: 986px; }
  .can-do-list li { height: 27px; }
  .can-do-list li::before { left: -18px; }

  .role-table {
    position: absolute; left: 61px; top: 608px; width: 719px;
    border-collapse: collapse; font-size: 12.6px;
  }
  .role-table th {
    background: var(--table-head); color: #fff; font-weight: 400;
    height: 67px; font-size: 12.6px; line-height: 15px; padding: 0 6px;
    border-left: 1px solid #fff;
  }
  .role-table th:first-child { border-left: none; }
  .role-table td {
    height: 35px; border: 1px solid var(--rule); padding: 0 6px; vertical-align: middle;
  }
</style>
</head>
<body>
<main class="page">
  <h2 class="section-band band-roles">1. User Roles and Permissions</h2>
  <p class="body-text intro-roles">The Web Editor Tool is allowed to be used to all the users that have edit permissions in their user role.</p>
  <h3 class="red-heading heading-roles">Currently, FDSF tool has the roles below:</h3>

  <ul class="list role-list">
    <li class="role" style="top:332px">Risk Administrator:</li>
    <li class="perm" style="top:364px">Can do everything into Verindo model</li>
    <li class="role" style="top:399px">Risk Project Leader</li>
    <li class="perm" style="top:428px">He can modify the report but NOT saving it or create a new one</li>
    <li class="perm" style="top:463px">He cannot move or delete the current reports stored at server</li>
    <li class="perm" style="top:497px">He cannot set permissions</li>
    <li class="role" style="top:533px">Risk Publisher</li>
    <li class="perm" style="top:561px">He can see the reports but do nothing more</li>
  </ul>

  <table class="role-table">
    <colgroup>
      <col style="width:198px"><col style="width:104px"><col style="width:187px"><col style="width:230px">
    </colgroup>
    <thead>
      <tr>
        <th>USER NAME</th>
        <th>CAN ACCESS TO WEB EDIT TOOL</th>
        <th>CAN MODIFY THE CURRENT REPORT BUT NO SAVING THIS</th>
        <th>CAN CREATE NEW REPORTS OR MODIFY THE CURRENT ONES</th>
      </tr>
    </thead>
    <tbody>
      <tr><td>RISK ADMINISTRATOR</td><td>YES</td><td>N/A</td><td>YES</td></tr>
      <tr><td>RISK PROJECT LEADER</td><td>YES</td><td>YES</td><td>NO</td></tr>
      <tr><td>RISK PUBLISHER</td><td>NO</td><td>NO</td><td>NO</td></tr>
    </tbody>
  </table>

  <h2 class="section-band band-restrictions">2. Restrictions using Web Editor Tool</h2>
  <p class="body-text intro-restrictions">Web Editor Tool contains big part of the current functionalities included at Verindo Desktop. This allows to the users to modify or create new reports online, without using Verindo Desktop. There are some rules that the users must bear in mind using the Web Editor Tool:</p>
  <h3 class="red-heading heading-can-do">What the Web Editor Tool users can do:</h3>

  <ul class="list can-do-list">
    <li>Create new views (sheets), duplicate, and rename views in a workbook</li>
    <li>Change aggregation of measures</li>
    <li>Use Show me to create views</li>
    <li>View underlying data</li>
    <li>Create and edit calculated fields, and use quick table calculations</li>
    <li>Drag field to different mark types in the Marks card</li>
  </ul>
</main>
</body>
</html>
```